Disease outbreak warning

I need a flyer that explains to hunters how to act as frontline responders to potential disease outbreaks in wildlife populations. In this case the disease is African Swine Fever. We need an at a glance style with plenty of colour and that’s very easy to read.

I HAVE ATTACHED SOME EXISTING FLYERS FROM OVERSEAS ETC THAT CONTAIN SOME OF THE RELEVANT INFO. THEY ARE TO BE USED AS A GUIDE ONLY.
Updates

Need to see some more options. We have some that can be developed successfully but we’d like to see some more options that will suit a national campaign.

Target Market(s)

Australian hunters encountering wild pigs. Typical age is from 18 to 32 but can be older. Male or female.

Colors

Designer to choose colors to be used in the design.

Requirements
Must have
• The KWOTL logo (supplied). It should be relatively small at the bottom of the page. Plus we need room for two or three other logos that can be overprinted on the project if required.
• Must have information for hunters as the main focus.
Nice to have
• A double sided flyer.
Should not have
• US spelling.

```html
<!DOCTYPE html>
<html lang="en-AU">
<head>
<meta charset="utf-8">
<title>African Swine Fever – Hunter Flyer</title>
<link rel="stylesheet" href="https://fonts.googleapis.com/css2?family=Oswald:wght@400;500;600;700&family=Roboto+Condensed:wght@400;500;700&family=Lato:wght@400;700&display=swap">
<style>
  :root {
    --olive: #3b3d24;
    --navy: #142b6c;
    --orange: #d3800b;
    --panel-grey: #dadadd;
    --ink: #1f1f22;
    --paper: #ffffff;
    --backdrop-top: #7b7b7b;
    --backdrop-bottom: #5d5d5d;
  }
  * { box-sizing: border-box; margin: 0; padding: 0; }
  html, body { width: 1200px; height: 1200px; overflow: hidden; }
  body {
    background: linear-gradient(180deg, var(--backdrop-top), var(--backdrop-bottom));
    font-family: "Roboto Condensed", "Arial Narrow", sans-serif;
    color: var(--ink);
    position: relative;
  }
  .page {
    position: absolute;
    width: 500px;
    height: 690px;
    background: var(--paper);
    overflow: hidden;
  }
  .page--front { left: 94px; top: 234px; }
  .page--back { left: 619px; top: 234px; }
  .abs { position: absolute; }

  .photo { position: absolute; }

  .brand {
    display: flex; align-items: center; gap: 6px;
    font-family: "Oswald", sans-serif; font-weight: 600;
    color: var(--navy);
  }
  .brand__dot {
    border-radius: 50%;
    background: var(--orange);
  }

  .title-band { position: absolute; left: 50px; top: 356px; width: 430px; height: 76px; }
  .title {
    position: absolute; left: 50px; top: 364px; width: 380px;
    text-align: center;
    font-family: "Oswald", sans-serif; font-weight: 700;
    font-size: 34px; letter-spacing: 0.2px;
    color: var(--paper); transform: scaleY(1.12);
  }
  .subtitle {
    position: absolute; left: 0; top: 437px; width: 500px;
    text-align: center;
    font-family: "Oswald", sans-serif; font-weight: 500; font-size: 17px;
    color: var(--ink);
  }
  .intro-pill {
    position: absolute; left: 86px; top: 470px; width: 323px; height: 60px;
    background: var(--navy); border-radius: 30px;
    color: var(--paper);
    font-family: "Lato", sans-serif; font-size: 8.6px; line-height: 11.2px;
    text-align: center;
    display: flex; align-items: center; justify-content: center;
    padding: 0 18px;
    box-shadow: 0 2px 3px rgba(0,0,0,0.25);
  }
  .tab {
    position: absolute; height: 29px;
    background: var(--orange); color: var(--paper);
    border-radius: 0 15px 15px 0;
    font-family: "Roboto Condensed", sans-serif; font-weight: 500;
    font-size: 8.8px; line-height: 10.5px;
    display: flex; align-items: center; padding-left: 9px;
  }
  .list {
    position: absolute;
    font-size: 6.8px; line-height: 9.2px; font-weight: 500;
    color: var(--ink);
  }
  .list--numbered { list-style: none; counter-reset: item; }
  .list--numbered li { counter-increment: item; }
  .list--numbered li::before { content: counter(item) ". "; color: var(--navy); }
  .list--dots { list-style: none; }
  .list--dots li { position: relative; padding-left: 10px; }
  .list--dots li::before {
    content: ""; position: absolute; left: 0; top: 3px;
    width: 3px; height: 3px; border-radius: 50%;
  }
  .list--orange li::before { background: var(--orange); }
  .list--navy li::before { background: var(--navy); }

  .divider { position: absolute; width: 1px; background: #c9c9cf; }

  .footer { position: absolute; left: 0; bottom: 0; width: 500px; height: 52px; }
  .footer__phone {
    position: absolute; left: 34px; bottom: 5px;
    display: flex; align-items: center; gap: 10px;
    font-family: "Oswald", sans-serif; font-weight: 600; font-size: 19px;
    color: var(--paper);
  }
  .footer__call {
    position: absolute; right: 35px; bottom: 6px;
    text-align: right;
    font-family: "Oswald", sans-serif; font-weight: 500;
    font-size: 12.6px; line-height: 16.5px;
    color: var(--paper);
  }

  .section-pill {
    position: absolute; left: 33px; top: 395px; width: 206px; height: 31px;
    background: var(--navy); color: var(--paper);
    border-radius: 0 16px 16px 0;
    font-family: "Oswald", sans-serif; font-weight: 600; font-size: 13px;
    display: flex; align-items: center; justify-content: center;
  }
  .donot-panel {
    position: absolute; left: 263px; top: 508px; width: 200px; height: 100px;
    background: var(--panel-grey); border-radius: 10px;
  }
  .donot-pill {
    position: absolute; left: 281px; top: 497px; width: 172px; height: 30px;
    background: var(--orange); color: var(--paper);
    border-radius: 15px;
    font-family: "Oswald", sans-serif; font-weight: 600; font-size: 20px;
    display: flex; align-items: center; justify-content: center;
  }
  .network-note {
    position: absolute; left: 48px; top: 625px; width: 164px;
    text-align: center; font-size: 5px; line-height: 6.4px;
    color: var(--navy); font-weight: 500;
  }
</style>
</head>
<body>

<!-- FRONT -->
<section class="page page--front">
  <svg class="photo" style="left:0;top:0" width="500" height="360" viewBox="0 0 500 360"
       role="img" aria-label="Photograph of a feral boar lying across a fallen log in open grassland, framed by a ragged paint-splash edge">
    <defs>
      <linearGradient id="frontScene" x1="0" y1="0" x2="0" y2="1">
        <stop offset="0" stop-color="#7ea7d3"/>
        <stop offset="0.18" stop-color="#7b7d55"/>
        <stop offset="0.4" stop-color="#5d7a3a"/>
        <stop offset="0.62" stop-color="#34332d"/>
        <stop offset="1" stop-color="#4a4337"/>
      </linearGradient>
    </defs>
    <path fill="url(#frontScene)" d="M190 40 C220 20 260 30 290 25 C320 10 350 30 380 5 L500 0 L500 120 C470 150 500 190 480 230 C470 260 495 290 470 310 C440 320 430 350 400 345 C370 340 360 360 330 350 C300 340 280 355 250 345 C220 340 200 360 170 340 C140 330 120 345 100 320 C80 310 90 290 60 270 C40 250 70 230 55 210 C40 190 60 170 90 160 C110 140 100 110 140 95 C160 80 150 60 190 40 Z"/>
  </svg>

  <div class="brand abs" style="left:18px;top:40px;font-size:20px;">
    <span class="brand__dot" style="width:16px;height:16px;"></span>KWOTL
  </div>

  <svg class="title-band" viewBox="0 0 430 76" aria-hidden="true">
    <path fill="var(--olive)" d="M12 8 L420 4 L430 22 L414 34 L428 50 L404 66 L300 72 L120 74 L20 70 L4 54 L16 40 L0 24 Z"/>
  </svg>
  <h1 class="title">AFRICAN SWINE FEVER</h1>
  <p class="subtitle">Hunters are on the Australian Biosecurity frontline</p>

  <div class="intro-pill">
    <p>African Swine Fever is on our doorstep and hunters should be on the lookout for any sign ASF has reached our shores. It has the potential to destroy Australia's domestic pork industry and cause wide-spread hunting bans. It must be contained.</p>
  </div>

  <div class="tab" style="left:34px;top:546px;width:196px;">The signs of African swine fever in pigs<br>can include:</div>
  <div class="tab" style="left:269px;top:546px;width:196px;">Inspect carcasses for:</div>
  <div class="divider" style="left:249px;top:545px;height:112px;"></div>

  <ol class="list list--numbered" style="left:35px;top:582px;width:205px;">
    <li>death (possibly before other signs are noticeable)</li>
    <li>blotching/reddening of the skin</li>
    <li>high fever</li>
    <li>lack of coordination or stiff gait</li>
    <li>difficulty breathing</li>
    <li>abortion</li>
    <li>diarrhoea</li>
    <li>vomiting</li>
  </ol>
  <ol class="list list--numbered" style="left:270px;top:582px;width:210px;">
    <li>pinpoint reddening in organs such as heart and kidneys</li>
    <li>reddening of the skin</li>
    <li>excess fluid around the heart</li>
    <li>enlarged lymph nodes resembling blood clots</li>
    <li>enlarged, fragile and/or dark-coloured spleen</li>
  </ol>

  <svg class="footer" viewBox="0 0 500 52" aria-hidden="true">
    <path fill="var(--orange)" d="M240 18 C246 8 252 3 264 2 L266 2 C256 4 252 10 248 18 Z"/>
    <path fill="var(--olive)" d="M0 21 L246 21 C252 8 258 3 268 2 L500 2 L500 52 L0 52 Z"/>
  </svg>
  <div class="footer__phone">
    <svg width="14" height="14" viewBox="0 0 24 24" aria-hidden="true"><path fill="#fff" d="M6.6 10.8c1.4 2.8 3.8 5.1 6.6 6.6l2.2-2.2c.3-.3.7-.4 1-.2 1.1.4 2.3.6 3.6.6.6 0 1 .4 1 1V20c0 .6-.4 1-1 1C10.6 21 3 13.4 3 4c0-.6.4-1 1-1h3.5c.6 0 1 .4 1 1 0 1.3.2 2.5.6 3.6.1.3 0 .7-.2 1L6.6 10.8z"/></svg>
    1800 555 210
  </div>
  <div class="footer__call">If you suspect ASF, call the<br>EmergencyAnimal Disease Hotline</div>
</section>

<!-- BACK -->
<section class="page page--back">
  <svg class="photo" style="left:0;top:0" width="500" height="480" viewBox="0 0 500 480"
       role="img" aria-label="Photograph of a feral boar lying across a fallen log with trees and grassland behind, framed by a ragged paint-splash edge">
    <defs>
      <linearGradient id="backScene" x1="0" y1="0" x2="0" y2="1">
        <stop offset="0" stop-color="#7fa9d6"/>
        <stop offset="0.16" stop-color="#6f7448"/>
        <stop offset="0.32" stop-color="#5f7f3c"/>
        <stop offset="0.6" stop-color="#302f2b"/>
        <stop offset="0.85" stop-color="#4b4437"/>
        <stop offset="1" stop-color="#3f4a2c"/>
      </linearGradient>
    </defs>
    <path fill="url(#backScene)" d="M50 0 L480 0 C490 20 470 30 500 50 L500 330 C485 350 495 380 470 400 C465 430 480 450 450 470 C420 480 390 470 360 475 C330 470 310 455 300 430 C290 405 300 390 285 375 C250 380 220 365 190 375 C150 385 130 365 100 375 C70 380 50 360 30 375 C10 380 0 365 0 360 L0 110 C20 90 10 70 30 60 C50 40 40 20 50 0 Z"/>
  </svg>

  <div class="section-pill">To prevent the spread of disease:</div>
  <ul class="list list--dots list--orange" style="left:36px;top:440px;width:210px;line-height:10.2px;font-size:7px;">
    <li>wear disposable or washable protective clothing (aprons / gloves / overalls) when dressing feral pigs</li>
    <li>inspect all carcasses and carcass parts for evidence of disease or illness</li>
    <li>clean and disinfect all equipment on site</li>
    <li>respect all quarantines, biosecurity plans and restrictions that are in place</li>
    <li>only hunt on one property each hunt</li>
    <li>thoroughly clean and disinfect vehicle after each hunt</li>
  </ul>

  <div class="divider" style="left:250px;top:374px;height:264px;"></div>

  <div class="brand abs" style="left:92px;top:566px;font-size:20px;">
    <span class="brand__dot" style="width:16px;height:16px;"></span>KWOTL
  </div>
  <p class="network-note">KWOTL, a part of the national<br>biosecurity network Ph 1300 555 417</p>

  <div class="donot-panel"></div>
  <div class="donot-pill">Do not</div>
  <ul class="list list--dots list--navy" style="left:270px;top:540px;width:195px;line-height:10.2px;font-size:7px;">
    <li>have contact with domestic pigs if you hunt feral pigs</li>
    <li>move live animals (including piglets) to new locations</li>
    <li>keep feral pigs at home</li>
    <li>use swill (meat and food scraps) to feed or trap feral pigs</li>
    <li>leave leftovers from your meals in the hunting area</li>
    <li>feed raw feral pork to dogs</li>
  </ul>

  <svg class="footer" viewBox="0 0 500 52" aria-hidden="true">
    <path fill="var(--orange)" d="M236 18 C242 8 248 3 260 2 L262 2 C252 4 248 10 244 18 Z"/>
    <path fill="var(--olive)" d="M0 21 L242 21 C248 8 254 3 264 2 L500 2 L500 52 L0 52 Z"/>
  </svg>
  <div class="footer__phone" style="left:35px;">
    <svg width="14" height="14" viewBox="0 0 24 24" aria-hidden="true"><path fill="#fff" d="M6.6 10.8c1.4 2.8 3.8 5.1 6.6 6.6l2.2-2.2c.3-.3.7-.4 1-.2 1.1.4 2.3.6 3.6.6.6 0 1 .4 1 1V20c0 .6-.4 1-1 1C10.6 21 3 13.4 3 4c0-.6.4-1 1-1h3.5c.6 0 1 .4 1 1 0 1.3.2 2.5.6 3.6.1.3 0 .7-.2 1L6.6 10.8z"/></svg>
    1800 555 210
  </div>
  <div class="footer__call">If you suspect ASF, call the<br>EmergencyAnimal Disease Hotline</div>
</section>

</body>
</html>
```